Book for new dads needs a cover.

We need a cover for a book titled Compass for Rookie Papas: Practical Steps for Surviving the Waiting Months, Juggling Jobs and Home, and Keeping Your Head Steady Before the Little One Arrives. We would like to see a design that emphasizes healthy babies and confident dads.

```html
<!DOCTYPE html>
<html lang="en">
<head>
<meta charset="utf-8">
<title>Compass for Rookie Papas — Book Cover</title>
<link rel="stylesheet" href="https://fonts.googleapis.com/css2?family=Anton&family=Inter:ital,wght@0,500;0,700;0,800;1,400&display=swap">
<style>
  :root {
    --stage: #262626;
    --paper: #ffffff;
    --orange: #ff7305;
    --blue: #0a5bab;
    --ink: #1f1f1f;
    --photo-light: #f4efea;
    --photo-mid: #d9cbbf;
    --photo-cool: #c9ced3;
  }
  html, body {
    margin: 0;
    padding: 0;
    width: 1200px;
    height: 1200px;
    overflow: hidden;
    background: var(--stage);
  }
  .cover {
    position: absolute;
    left: 216px;
    top: 25px;
    width: 767px;
    height: 1150px;
    background: var(--paper);
    overflow: hidden;
    font-family: "Inter", Arial, sans-serif;
  }
  .author {
    position: absolute;
    top: 70px;
    left: 0;
    width: 100%;
    display: flex;
    align-items: center;
    justify-content: center;
    gap: 12px;
  }
  .author-rule {
    width: 190px;
    height: 2px;
    background: var(--blue);
  }
  .author-name {
    font-weight: 800;
    font-size: 31px;
    letter-spacing: -1px;
    color: var(--blue);
    line-height: 1;
  }
  .title {
    position: absolute;
    left: 0;
    top: 0;
    width: 767px;
    height: 560px;
  }
  .title-word {
    font-family: "Anton", "Impact", sans-serif;
    fill: var(--orange);
  }
  .title-band-text {
    font-family: "Inter", Arial, sans-serif;
    font-weight: 800;
    fill: var(--paper);
  }
  .subtitle {
    position: absolute;
    top: 560px;
    left: 40px;
    width: 687px;
    text-align: center;
    margin: 0;
  }
  .subtitle-lead {
    display: block;
    font-weight: 700;
    font-size: 22px;
    color: var(--blue);
    line-height: 1.2;
    margin-bottom: 4px;
  }
  .subtitle-rest {
    display: block;
    font-style: italic;
    font-weight: 400;
    font-size: 19.5px;
    color: var(--ink);
    line-height: 1.4;
  }
  .photo {
    position: absolute;
    left: 90px;
    top: 650px;
    width: 600px;
    height: 500px;
    border-radius: 300px 300px 0 0;
    background: radial-gradient(ellipse at 50% 45%, var(--photo-mid) 0%, var(--photo-light) 55%, var(--paper) 100%),
                linear-gradient(180deg, var(--photo-light), var(--photo-cool));
    background-blend-mode: multiply;
  }
</style>
</head>
<body>
  <main class="cover">
    <div class="author">
      <span class="author-rule"></span>
      <span class="author-name">AUTHOR NAME</span>
      <span class="author-rule"></span>
    </div>

    <svg class="title" viewBox="0 0 767 560" aria-label="Compass for Rookie Papas">
      <text class="title-word" x="53" y="233" font-size="152" textLength="663" lengthAdjust="spacingAndGlyphs">COMPASS</text>
      <text class="title-word" x="119" y="518" font-size="340" textLength="533" lengthAdjust="spacingAndGlyphs">PAPAS</text>
      <g transform="rotate(-4.5 383 264)">
        <rect x="202" y="224" width="362" height="80" rx="6" fill="var(--blue)"/>
        <text class="title-band-text" x="383" y="277" font-size="36" text-anchor="middle" letter-spacing="1">FOR ROOKIE</text>
      </g>
    </svg>

    <p class="subtitle">
      <span class="subtitle-lead">Practical Steps for Surviving the Waiting Months,</span>
      <span class="subtitle-rest">Juggling Jobs and Home, and Keeping Your Head Steady<br>Before the Little One Arrives.</span>
    </p>

    <div class="photo" role="img" aria-label="Photo of a smiling father in a grey hoodie holding his laughing baby close"></div>
  </main>
</body>
</html>
```